Flyer Design

I need a nice professional flyer design to use for advertising my lawn/snow removal business. Flyers I am using are 5.47"x4.21". I've attached a flyer I found online that I liked. Just wanting something creative and professional. The images of the logos I attached are of the original logo design, and the new color design we are using. There is also a mockup of our tshirt design to give you an idea of the actual color on the tshirt, since the jpeg logo isn't exactly accurate on color.
Things I need on the flyer in no particular order:
"Snow is coming"
"Don't Wait Until It's TOO LATE!"
"Free Estimates"
Services offered
"Commercial/Residential"
"Snow Plowing"
"Snow Blowing"
"Snow Shoveling"
"Ice Removal"
"Salting/Sanding"
"Fully Licensed and Insured"
"Available and ON CALL 24/7"
"Seasonal Packages Available"
"CALL NOW TO RESERVE"

```html
<!DOCTYPE html>
<html lang="en">
<head>
<meta charset="utf-8">
<title>Fieldcrest Lawn &amp; Landscape – Snow Services Flyer</title>
<link href="https://fonts.googleapis.com/css2?family=Noto+Serif:wght@400;700&family=Open+Sans:wght@600;700;800&family=Lato:wght@400&display=swap" rel="stylesheet">
<style>
  :root {
    --page-bg: #e9e6e2;
    --navy: #0b2a52;
    --sky-blue: #2f80d8;
    --box-orange: #f24a06;
    --head-orange: #f05516;
    --text-orange: #f47b2a;
    --ink: #141414;
    --white: #ffffff;
    --snow-light: #f4f4f4;
    --snow-mid: #d9dadc;
  }
  * { margin: 0; padding: 0; box-sizing: border-box; }
  html, body { width: 1200px; height: 1199px; overflow: hidden; background: var(--page-bg); }
  .flyer {
    position: absolute; left: 50px; top: 176px;
    width: 1100px; height: 848px; overflow: hidden;
    background: var(--navy);
    box-shadow: 0 6px 18px rgba(0,0,0,.25);
    font-family: "Noto Serif", serif;
  }
  .flyer__art { position: absolute; inset: 0; }
  .headline {
    position: absolute; right: 26px; top: 16px;
    font-weight: 700; font-size: 78px; line-height: 1; color: var(--head-orange);
    letter-spacing: -0.5px;
  }
  .subline {
    position: absolute; right: 28px; top: 110px;
    font-weight: 700; font-size: 34px; line-height: 1; color: var(--ink);
  }
  .brand {
    position: absolute; left: 600px; top: 268px; width: 430px;
    display: flex; align-items: center; gap: 18px;
  }
  .brand__dot { width: 58px; height: 58px; border-radius: 50%; background: var(--box-orange); flex: none; }
  .brand__name { font-weight: 700; font-size: 40px; line-height: 1.1; color: var(--navy); }
  .services {
    position: absolute; left: 72px; top: 365px; width: 439px; height: 442px;
    background: var(--box-orange); border-radius: 9px; color: var(--white);
    box-shadow: 0 3px 8px rgba(0,0,0,.3);
  }
  .services__title { position: absolute; left: 27px; top: 18px; font-weight: 700; font-size: 46px; line-height: 1.1; }
  .services__sectors { position: absolute; left: 31px; top: 82px; font-family: "Lato", sans-serif; font-size: 31px; }
  .services__list { position: absolute; left: 40px; top: 145px; list-style: none; }
  .services__item {
    display: flex; align-items: center; gap: 24px; height: 53px;
    font-family: "Open Sans", sans-serif; font-weight: 700; font-size: 32px;
  }
  .services__tick { width: 32px; height: 32px; flex: none; }
  .info { position: absolute; left: 540px; width: 540px; text-align: center; line-height: 1; }
  .info--licensed { top: 507px; font-size: 31px; color: var(--sky-blue); }
  .info--oncall { top: 543px; font-size: 31px; color: var(--text-orange); }
  .info--seasonal { top: 579px; font-size: 31px; color: var(--sky-blue); }
  .info--reserve { top: 636px; font-size: 43px; font-weight: 700; color: var(--text-orange); }
  .info--phone { top: 685px; font-family: "Open Sans", sans-serif; font-weight: 800; font-size: 72px; color: var(--text-orange); letter-spacing: -1px; }
  .info--estimates { top: 768px; font-size: 42px; font-weight: 700; color: var(--white); }
</style>
</head>
<body>
<main class="flyer">
  <svg class="flyer__art" width="1100" height="848" viewBox="0 0 1100 848">
    <defs>
      <linearGradient id="snow-scene" x1="0" y1="0" x2="1" y2="1">
        <stop offset="0" stop-color="var(--snow-mid)"/>
        <stop offset=".5" stop-color="var(--snow-light)"/>
        <stop offset="1" stop-color="#e7e8ea"/>
      </linearGradient>
    </defs>
    <rect role="img" aria-label="Photo of a white pickup truck with a red snow plow clearing a snowy road" x="0" y="0" width="1100" height="460" fill="url(#snow-scene)"/>
    <path class="wave-stripe" d="M0 168 C150 250 300 330 520 412 C700 430 900 426 1100 420 L1100 848 L0 848 Z" fill="var(--sky-blue)"/>
    <path class="wave-navy" d="M0 180 C150 262 300 342 520 424 C700 442 900 438 1100 432 L1100 848 L0 848 Z" fill="var(--navy)"/>
  </svg>

  <h1 class="headline">Snow is coming</h1>
  <p class="subline">Don't Wait Until It's TOO LATE!</p>

  <div class="brand">
    <span class="brand__dot"></span>
    <span class="brand__name">Fieldcrest Lawn<br>&amp; Landscape</span>
  </div>

  <section class="services">
    <h2 class="services__title">Services Offered</h2>
    <p class="services__sectors">Commercial - Residential</p>
    <ul class="services__list">
      <li class="services__item"><svg class="services__tick" viewBox="0 0 32 32"><circle cx="16" cy="16" r="14" fill="var(--white)"/><path d="M9 16 l5 5 l10-11" fill="none" stroke="var(--box-orange)" stroke-width="4" stroke-linecap="round" stroke-linejoin="round"/></svg>Snow Plowing</li>
      <li class="services__item"><svg class="services__tick" viewBox="0 0 32 32"><circle cx="16" cy="16" r="14" fill="var(--white)"/><path d="M9 16 l5 5 l10-11" fill="none" stroke="var(--box-orange)" stroke-width="4" stroke-linecap="round" stroke-linejoin="round"/></svg>Snow Blowing</li>
      <li class="services__item"><svg class="services__tick" viewBox="0 0 32 32"><circle cx="16" cy="16" r="14" fill="var(--white)"/><path d="M9 16 l5 5 l10-11" fill="none" stroke="var(--box-orange)" stroke-width="4" stroke-linecap="round" stroke-linejoin="round"/></svg>Snow Shoveling</li>
      <li class="services__item"><svg class="services__tick" viewBox="0 0 32 32"><circle cx="16" cy="16" r="14" fill="var(--white)"/><path d="M9 16 l5 5 l10-11" fill="none" stroke="var(--box-orange)" stroke-width="4" stroke-linecap="round" stroke-linejoin="round"/></svg>Ice Removal</li>
      <li class="services__item"><svg class="services__tick" viewBox="0 0 32 32"><circle cx="16" cy="16" r="14" fill="var(--white)"/><path d="M9 16 l5 5 l10-11" fill="none" stroke="var(--box-orange)" stroke-width="4" stroke-linecap="round" stroke-linejoin="round"/></svg>Salting/Sanding</li>
    </ul>
  </section>

  <p class="info info--licensed">Fully Licensed and Insured</p>
  <p class="info info--oncall">AVAILABLE AND ON CALL 24/7</p>
  <p class="info info--seasonal">Seasonal Packages Available</p>
  <p class="info info--reserve">Call Now to Reserve</p>
  <p class="info info--phone">123-456-7890</p>
  <p class="info info--estimates">Free Estimates</p>
</main>
</body>
</html>
```